Painting Contractor Business Card Design

We are looking for a cool, bold, modern, polished, business card design. We are a high-end residential painting contractor. Please incorporate our logo and keep with our green/black color scheme. We are interested in seeing 2-sided and 1-sided options. Thank you very much!

Industry/Entity Type

Business

Contact Information for Business Card

Info for the card:
Owen Talsky
mobile 206-555-0193
email owen@kestrowfinish.net
web www.kestrowfinish.net

```html
<!DOCTYPE html>
<html lang="en">
<head>
<meta charset="utf-8">
<title>Kestrow Finish – Business Card</title>
<link rel="stylesheet" href="https://fonts.googleapis.com/css2?family=Open+Sans:wght@400;600;700&display=swap">
<style>
  :root {
    --ink: #1b1b1c;
    --paper: #ffffff;
    --accent-blue: #2f7fd0;
    --accent-green: #35b34a;
    --text: #222222;
    --backdrop: #e9e7e3;
  }
  * { margin: 0; padding: 0; box-sizing: border-box; }
  html, body {
    width: 1200px; height: 900px; overflow: hidden;
    background: var(--backdrop);
    font-family: "Open Sans", Arial, sans-serif;
    color: var(--text);
  }
  .card {
    position: absolute; left: 250px; width: 700px; height: 400px;
    background: var(--paper);
    box-shadow: 0 8px 24px rgba(0,0,0,.18);
    overflow: hidden;
  }
  .card--back { top: 40px; }
  .card--front { top: 470px; }

  .band { position: absolute; left: 0; width: 100%; }
  .band--ink { background: var(--ink); }
  .band--rule { height: 3px; background: var(--accent-blue); }

  /* back */
  .back-mark {
    position: absolute; left: 0; right: 0; top: 37px; height: 326px;
    display: flex; align-items: center; justify-content: center; gap: 22px;
  }
  .brand-square { width: 58px; height: 58px; background: var(--accent-green); flex: none; }
  .brand-name {
    font-weight: 700; letter-spacing: 2px; text-transform: uppercase; white-space: nowrap;
  }
  .back-mark .brand-name { color: var(--paper); font-size: 44px; }

  /* front */
  .front-brand {
    position: absolute; left: 40px; top: 70px;
    display: flex; align-items: center; gap: 18px;
  }
  .front-brand .brand-square { width: 46px; height: 46px; }
  .front-brand .brand-name { color: var(--ink); font-size: 38px; }
  .brand-rule {
    position: absolute; left: 40px; right: 30px; top: 138px; height: 1.5px; background: var(--ink);
  }
  .name-plate {
    position: absolute; left: 40px; top: 200px; width: 270px; height: 84px;
    background: var(--ink); padding: 14px 24px;
  }
  .name-plate .person { color: var(--paper); font-size: 27px; font-weight: 700; line-height: 1.2; }
  .name-plate .role { color: var(--accent-blue); font-size: 15px; line-height: 1.2; }
  .contact-list {
    position: absolute; left: 370px; top: 160px; width: 300px; list-style: none;
  }
  .contact-list li {
    font-size: 15px; padding: 8px 0 6px; border-bottom: 1.5px solid var(--accent-green);
    white-space: nowrap;
  }
</style>
</head>
<body>
  <section class="card card--back" aria-label="Card back">
    <div class="band band--rule" style="top:34px"></div>
    <div class="band band--ink" style="top:37px;height:326px"></div>
    <div class="band band--rule" style="top:363px"></div>
    <div class="back-mark">
      <span class="brand-square"></span>
      <span class="brand-name">Kestrow Finish</span>
    </div>
  </section>

  <section class="card card--front" aria-label="Card front">
    <div class="band band--ink" style="top:0;height:34px"></div>
    <div class="band band--rule" style="top:44px"></div>
    <div class="front-brand">
      <span class="brand-square"></span>
      <span class="brand-name">Kestrow Finish</span>
    </div>
    <div class="brand-rule"></div>
    <div class="name-plate">
      <p class="person">Owen Talsky</p>
      <p class="role">Owner</p>
    </div>
    <ul class="contact-list">
      <li>Mobile: 206-555-0193</li>
      <li>Email: owen@kestrowfinish.net</li>
      <li>Website: www.kestrowfinish.net</li>
    </ul>
    <div class="band band--rule" style="top:322px"></div>
    <div class="band band--ink" style="top:334px;height:32px"></div>
    <div class="band band--ink" style="top:378px;height:22px"></div>
  </section>
</body>
</html>
```